Zielgruppe
Ich biete Menschen, die in ihrem Beruf hohen Stressbelastungen ausgesetzt sind, schnelle und wirksame Hilfe. Sie können bei mir lernen, langfristig ohne Stress in ihrem Job erfolgreich zu sein.
Mein Angebot nennt sich „Mit Ruhe ans Ziel“. Es besteht aus drei Bausteinen, einem wissenschaftlichem Stresstest, intensiven Kleingruppen-Workshops und individuellem Einzelcoaching.
So kann ich flexibel für jeden die passende Lösungsstrategie zur Stressbewältigung anbieten.
Aufgabenstellung
Farbwelt des Logos Mit Ruhe ans Ziel berücksichtigen
Persönlichen Daten/Adressdaten auf der Vorderseite:
Marlene Wudrich
Personal/Business Coach
Stressmanagement-Trainerin
Beraterin für KALMIS Belastungsschutz by Feuring®
Lindauer Weg 17
10482 Berlin
Tel: (030) 41862270
Mobil: (0173) 2904815
Email: info@mit-ruhe-ans-ziel.de
Text auf der Rückseite:
Mit Ruhe ans Ziel:
Wissenschaftlicher Stresstest KALMIS
Intensive Kleingruppen-Workshops
Individuelles Coaching
www.mit-ruhe-ans-ziel.de

```html
<!DOCTYPE html>
<html lang="de">
<head>
<meta charset="utf-8">
<title>Mit Ruhe ans Ziel – Visitenkarte</title>
<link href="https://fonts.googleapis.com/css2?family=Ubuntu:wght@300;400;500;700&display=swap" rel="stylesheet">
<style>
  :root {
    --page-bg: #f1f2f4;
    --card-white: #ffffff;
    --card-dark: #555a55;
    --green: #7ab648;
    --rose: #b5587a;
    --ink: #3a3a3a;
    --ink-soft: #4a4a4a;
    --light-text: #e6e6e6;
    --shadow: 0 8px 14px rgba(0,0,0,0.18);
  }
  * { margin: 0; padding: 0; box-sizing: border-box; }
  html, body {
    width: 849px; height: 1200px; overflow: hidden;
    background: var(--page-bg);
    font-family: "Ubuntu", sans-serif;
  }
  .sheet { position: relative; width: 849px; height: 1200px; }

  .wordmark {
    position: absolute; display: flex; align-items: center; gap: 8px;
    color: var(--green); font-weight: 500; white-space: nowrap;
  }
  .wordmark .dot {
    width: 0.38em; height: 0.38em; border-radius: 50%; background: var(--rose);
  }
  .wordmark--hero { top: 380px; left: 0; width: 849px; justify-content: center; font-size: 36px; }

  .card {
    position: absolute; top: 440px; width: 373px; height: 241px;
    box-shadow: var(--shadow);
  }
  .card--front { left: 37px; background: var(--card-white); border-left: 5px solid var(--green); }
  .card--back { left: 438px; background: var(--card-dark); }

  .card .wordmark { top: 30px; font-size: 24px; }
  .card--front .wordmark { left: 54px; }
  .card--back .wordmark { left: 62px; }

  .holder {
    position: absolute; left: 55px; top: 90px;
    font-size: 10px; font-weight: 500; color: var(--ink);
  }
  .services {
    position: absolute; list-style: none; font-size: 10px; font-weight: 300; line-height: 14.8px;
  }
  .services li::before {
    content: ""; display: inline-block; width: 4px; height: 4px; border-radius: 50%;
    background: var(--rose); margin-right: 5px; vertical-align: middle; position: relative; top: -1px;
  }
  .card--front .services { left: 55px; top: 110px; color: var(--ink-soft); font-weight: 400; }
  .card--back .services { left: 96px; top: 110px; color: var(--light-text); }

  .address {
    position: absolute; left: 41px; top: 195px;
    font-size: 9.5px; line-height: 14px; color: var(--ink-soft); font-style: normal;
  }
  .divider {
    position: absolute; left: 172px; top: 176px; width: 1.5px; height: 65px; background: var(--rose);
  }
  .contacts {
    position: absolute; left: 185px; top: 181px; list-style: none;
    font-size: 9.5px; line-height: 14px; color: var(--ink-soft);
  }
  .contacts li { display: flex; align-items: center; gap: 6px; }
  .contacts svg { width: 9px; height: 9px; fill: var(--rose); flex: none; }

  .website {
    position: absolute; left: 90px; top: 204px;
    font-size: 12.5px; font-weight: 500; color: var(--green);
  }
</style>
</head>
<body>
<main class="sheet">

  <div class="wordmark wordmark--hero"><span class="dot"></span>Mit Ruhe ans Ziel</div>

  <section class="card card--front" aria-label="Vorderseite">
    <div class="wordmark"><span class="dot"></span>Mit Ruhe ans Ziel</div>
    <p class="holder">Marlene Wudrich</p>
    <ul class="services">
      <li>Personal/Business Coach</li>
      <li>Stressmanagement-Trainerin</li>
      <li>Beraterin für KALMIS Belastungsschutz by Feuring®</li>
    </ul>
    <address class="address">Lindauer Weg 17<br>10482 Berlin</address>
    <div class="divider"></div>
    <ul class="contacts">
      <li>
        <svg viewBox="0 0 10 10" aria-hidden="true"><path d="M2 0.5 L3.6 0.5 L4.2 3 L3 3.8 Q4 6 6.2 7 L7 5.8 L9.5 6.4 L9.5 8 Q9.5 9.5 8 9.5 Q0.5 9 0.5 2 Q0.5 0.5 2 0.5Z"/></svg>
        (030) 41862270
      </li>
      <li>
        <svg viewBox="0 0 10 10" aria-hidden="true"><path d="M2.5 0 H7.5 Q8.5 0 8.5 1 V9 Q8.5 10 7.5 10 H2.5 Q1.5 10 1.5 9 V1 Q1.5 0 2.5 0Z M2.7 1.2 V7.8 H7.3 V1.2Z"/></svg>
        (0173) 2904815
      </li>
      <li>
        <svg viewBox="0 0 10 10" aria-hidden="true"><path d="M0.5 2 H9.5 V8.5 H0.5Z M1.2 2.6 L5 5.6 L8.8 2.6" stroke="#fff" stroke-width="0.7"/></svg>
        info@mit-ruhe-ans-ziel.de
      </li>
    </ul>
  </section>

  <section class="card card--back" aria-label="Rückseite">
    <div class="wordmark"><span class="dot"></span>Mit Ruhe ans Ziel</div>
    <ul class="services">
      <li>Wissenschaftlicher Stresstest KALMIS</li>
      <li>Intensive Kleingruppen-Workshops</li>
      <li>Individuelles Coaching</li>
    </ul>
    <p class="website">www.mit-ruhe-ans-ziel.de</p>
  </section>

</main>
</body>
</html>
```